I need a book cover (front and back) for a book I wrote called "7 Habits of Dress: A Closet Map for Growth".

The short version of the book can be found online here: https://filebinder.example/doc/7QkZ-pLm3Rt8yXvB2NcWd9HsJf4GaE/open

I'm working on expanding this into a real book (100+ pages, with images), and putting it on Brindlo.

I'm the author, Milo Vashenko. I was named "Finest Groomed Gent in America" by Dapperline Journal, and I would like to add that to the cover for credibility.

My website "About Page" has more info about me and my business Threads of Merit: https://threadsofmerit.example/pages/about-us

I also attached the first version of the cover I made using Canva.

I have LOTS of images, if you need some (mannequins, models, garments, etc). See our website's blog for more ideas of the images we have: https://threadsofmerit.example/blogs/news

```html
<!DOCTYPE html>
<html lang="en">
<head>
<meta charset="utf-8">
<title>Seven Habits of Dress — Cover Spread</title>
<link rel="stylesheet" href="https://fonts.googleapis.com/css2?family=Montserrat:wght@400;500;600&display=swap">
<style>
  :root {
    --stage: #fbc962;
    --cover: #141516;
    --cover-edge: #0b0b0c;
    --cover-glow: #2a2c2e;
    --ink: #f2f2f2;
    --ink-soft: #c9ced2;
    --title: #5c6a73;
    --photo-top: #3b3f42;
    --photo-mid: #2c3236;
    --photo-low: #1b1f22;
    --portrait-wall: #6b4a3c;
    --portrait-suit: #2f4f86;
  }
  * { box-sizing: border-box; margin: 0; padding: 0; }
  html, body { width: 1200px; height: 960px; overflow: hidden; }
  body {
    background: var(--stage);
    font-family: "Montserrat", sans-serif;
    color: var(--ink);
    position: relative;
  }
  .spread {
    position: absolute;
    left: 60px; top: 100px;
    width: 1080px; height: 760px;
    display: flex;
  }
  .cover {
    width: 540px; height: 760px;
    position: relative;
    background: radial-gradient(ellipse at 50% 30%, var(--cover-glow) 0%, var(--cover) 65%);
    border: 1px solid var(--cover-edge);
    overflow: hidden;
  }
  .cover--back { border-right: 2px solid var(--cover-edge); }

  /* Back cover */
  .author-heading {
    position: absolute; top: 40px; left: 0; right: 0;
    text-align: center;
    font-weight: 600; font-size: 24px; letter-spacing: 6px;
  }
  .bio-intro {
    position: absolute; left: 66px; top: 98px; width: 218px;
    font-size: 13px; font-weight: 500; line-height: 27px; text-align: justify;
    text-indent: 40px;
  }
  .author-portrait {
    position: absolute; left: 300px; top: 102px;
    width: 185px; height: 252px;
    background: linear-gradient(180deg, var(--portrait-wall) 0%, var(--portrait-wall) 30%, var(--portrait-suit) 55%, #24406e 100%);
  }
  .bio-more {
    position: absolute; left: 68px; top: 370px; width: 416px;
    font-size: 13px; font-weight: 500; line-height: 27px; text-align: justify;
  }

  /* Front cover */
  .cover-photo {
    position: absolute; left: 100px; top: 30px;
    width: 340px; height: 650px;
    border-radius: 170px 170px 20px 20px;
    background: linear-gradient(180deg, var(--photo-top) 0%, var(--photo-mid) 45%, var(--photo-low) 100%);
  }
  .cover-title {
    position: absolute; left: 0; right: 0; top: 140px;
    text-align: center;
    font-weight: 500; font-size: 84px; line-height: 104px;
    color: var(--title);
    letter-spacing: -1px;
  }
  .cover-subtitle {
    position: absolute; left: 0; right: 0; top: 578px;
    text-align: center;
    font-weight: 500; font-size: 18px; letter-spacing: 2px;
    color: var(--ink-soft);
  }
  .cover-credential {
    position: absolute; left: 0; right: 0; top: 618px;
    text-align: center;
    font-weight: 500; font-size: 12px; letter-spacing: 1px;
    color: var(--ink-soft);
  }
  .cover-author {
    position: absolute; left: 0; right: 0; bottom: 38px;
    text-align: center;
    font-weight: 600; font-size: 24px; letter-spacing: 6px;
  }
</style>
</head>
<body>
  <main class="spread">
    <section class="cover cover--back">
      <h2 class="author-heading">MILO VASHENKO</h2>
      <p class="bio-intro">Milo Vashenko was named “America’s Finest Groomed Gent” by Dapperline Journal while studying psychology at Halden University. He then trained to become a bespoke tailor and earned a degree in Menswear Design from the Meridian Institute of Design.</p>
      <div class="author-portrait" role="img" aria-label="Portrait of the author in a blue three-piece suit against a brick wall"></div>
      <p class="bio-more">After ten years of working with customers in New York City, Milo combined his experience in bespoke tailoring with his passion for teaching men how to dress for success and created Threads of Merit.<br>Milo lives in Toronto with his wife Elena and their daughter Nadia where he works with customers from allover the world to improve their style and refine their wardrobes.</p>
    </section>
    <section class="cover cover--front">
      <div class="cover-photo" role="img" aria-label="Photograph of a bearded man in a fedora, sunglasses and dark tweed jacket"></div>
      <h1 class="cover-title">SEVEN<br>HABITS<br>OF<br>DRESS</h1>
      <p class="cover-subtitle">A Closet Map for Growth</p>
      <p class="cover-credential">“Finest Groomed Gent in America” — Dapperline Journal</p>
      <p class="cover-author">MILO VASHENKO</p>
    </section>
  </main>
</body>
</html>
```